showcase project portfolio

create power point of project portfolio
from word file and website using similar design template

https://www.brelvon.co.uk/

Target Market(s)

corporte

```html
<!DOCTYPE html>
<html lang="en">
<head>
<meta charset="utf-8">
<title>Brelvon Design Solutions – Project Portfolio</title>
<link href="https://fonts.googleapis.com/css2?family=Josefin+Sans:wght@300;400;600&display=swap" rel="stylesheet">
<style>
  :root {
    --page: #b3b3b3;
    --navy: #1f3a52;
    --navy-dark: #1a3147;
    --tan: #c9a58a;
    --tan-light: #e9d8cb;
    --white: #ffffff;
    --ink: #1b1b1b;
    --muted: #5d6b78;
    --brick-a: #8b5a44;
    --brick-b: #b07a5c;
    --sky: #b9c3c8;
    --plan: #f4f2e2;
  }
  * { box-sizing: border-box; margin: 0; padding: 0; }
  html, body { width: 849px; height: 1200px; overflow: hidden; }
  body {
    background: var(--page);
    font-family: "Josefin Sans", sans-serif;
    color: var(--ink);
    position: relative;
  }
  .slide {
    position: absolute;
    width: 387px;
    height: 216px;
    background: var(--white);
    overflow: hidden;
  }
  .slide-cover { left: 231px; top: 32px; }
  .slide-tasks { left: 32px; top: 268px; }
  .slide-p1 { left: 430px; top: 268px; }
  .slide-p2 { left: 32px; top: 496px; }
  .slide-p3 { left: 430px; top: 496px; }
  .slide-p4 { left: 32px; top: 725px; }
  .slide-p5 { left: 430px; top: 725px; }
  .slide-contact { left: 231px; top: 953px; }

  .header-band { position: absolute; left: 0; top: 0; width: 387px; height: 100px; }
  .slide-title {
    position: absolute; left: 0; right: 0; top: 11px;
    text-align: center; color: var(--white);
    font-weight: 300; font-size: 19px; letter-spacing: 1.2px;
  }
  .slide-title span { display: inline-block; border-bottom: 1px solid var(--tan); padding-bottom: 1px; }

  .info-row { position: absolute; display: flex; align-items: flex-start; gap: 3px; }
  .info-label {
    background: var(--navy-dark); color: var(--white);
    font-size: 5.6px; letter-spacing: .4px; padding: 2px 3px 1px;
    white-space: nowrap;
  }
  .info-text { color: var(--white); font-size: 5.6px; line-height: 6.6px; padding-top: 1px; font-weight: 300; }

  .visual { position: absolute; border: 1.2px solid var(--navy); }
  .visual-photo { background: linear-gradient(160deg, var(--sky) 0%, var(--brick-b) 45%, var(--brick-a) 100%); }
  .visual-photo.green { background: linear-gradient(160deg, #6f8a5a 0%, var(--brick-b) 50%, #5a4a3c 100%); }
  .visual-photo.grey { background: linear-gradient(170deg, #c7cdd2 0%, #8c8478 50%, #56534f 100%); }
  .visual-drawing { background: linear-gradient(180deg, var(--white), #eceff1); }
  .visual-drawing.coloured { background: linear-gradient(90deg, var(--plan), #eef4c8 60%, var(--white)); }

  /* cover */
  .cover-bg { position: absolute; inset: 0; background: linear-gradient(180deg, #3f5a6e 0%, #2c4a60 55%, #324d5f 100%); }
  .brand-mark { position: absolute; left: 0; right: 0; text-align: center; }
  .brand-mark .brand-name { font-weight: 600; font-size: 22px; letter-spacing: 3px; color: var(--tan); }
  .brand-mark .brand-sub { font-size: 5px; letter-spacing: .6px; color: var(--tan); margin-top: 2px; }
  .cover-tagline { position: absolute; top: 118px; left: 0; right: 0; text-align: center; color: var(--white); font-weight: 300; font-size: 9.5px; letter-spacing: .9px; }
  .cover-managed {
    position: absolute; top: 172px; left: 124px; width: 139px; height: 6px;
    background: linear-gradient(90deg, transparent, var(--tan) 20%, var(--tan) 80%, transparent);
    text-align: center; font-size: 4.2px; line-height: 6.4px; letter-spacing: .5px; color: var(--navy-dark);
  }
  .cover-company { position: absolute; top: 180px; left: 0; right: 0; text-align: center; color: var(--white); font-weight: 300; }
  .cover-company .line1 { font-size: 13px; letter-spacing: 1px; }
  .cover-company .line2 { font-size: 7px; letter-spacing: 1.3px; }

  /* tasks */
  .tasks-photo {
    position: absolute; left: 0; top: 0; width: 387px; height: 100px;
    background: linear-gradient(170deg, #d9dee0 0%, #b07458 40%, #7d4b36 100%);
    clip-path: polygon(0 0, 100% 0, 100% 55%, 50% 100%, 0 78%);
  }
  .tasks-strip { position: absolute; left: 0; top: 0; width: 387px; height: 104px; }
  .tasks-brand { position: absolute; left: 26px; top: 118px; width: 80px; text-align: center; }
  .tasks-brand .brand-name { font-weight: 600; font-size: 14px; letter-spacing: 1.5px; color: var(--navy); }
  .tasks-brand .brand-sub { font-size: 4.2px; color: var(--navy); margin-top: 2px; }
  .tasks-brand .brand-square { width: 10px; height: 10px; background: var(--tan); margin: 0 auto 4px; }
  .tasks-label {
    position: absolute; left: 27px; top: 187px; width: 76px; height: 16px;
    background: var(--navy-dark); color: var(--white);
    clip-path: polygon(0 0, 86% 0, 100% 50%, 86% 100%, 0 100%);
    font-weight: 300; font-size: 12px; letter-spacing: 2.5px; line-height: 17px; padding-left: 7px;
  }
  .task-list { position: absolute; left: 127px; top: 106px; list-style: none; }
  .task-list li { font-size: 6px; line-height: 7.3px; display: flex; gap: 3px; align-items: center; white-space: nowrap; }
  .task-list svg { width: 5px; height: 5px; flex: none; }

  /* contact */
  .contact-text { position: absolute; top: 41px; left: 0; right: 0; text-align: center; color: var(--white); font-size: 6px; line-height: 7.3px; font-weight: 300; }
  .contact-brand { top: 105px; }
  .contact-brand .brand-name { color: var(--navy); font-size: 18px; }
  .contact-brand .brand-sub { color: var(--navy); font-size: 4.5px; }
  .contact-card {
    position: absolute; top: 155px; width: 100px; height: 53px;
    background: var(--navy-dark); color: var(--white);
    display: flex; flex-direction: column; align-items: center; justify-content: center;
    font-size: 5.6px; line-height: 6.6px; text-align: center; gap: 3px; font-weight: 300;
  }
  .contact-card svg { width: 9px; height: 9px; }
  .card-phone { left: 38px; }
  .card-address { left: 143px; }
  .card-web { left: 248px; }
</style>
</head>
<body>

<svg width="0" height="0" style="position:absolute" aria-hidden="true">
  <defs>
    <linearGradient id="band-gradient" x1="0" y1="0" x2="0" y2="1">
      <stop offset="0" stop-color="#1f3a52"/>
      <stop offset="0.45" stop-color="#3b4a5a"/>
      <stop offset="1" stop-color="#c9a58a"/>
    </linearGradient>
    <symbol id="header-band" viewBox="0 0 387 100">
      <polygon points="0,62 387,62 387,68 193.5,98 0,68" fill="#e9d8cb"/>
      <polygon points="0,0 387,0 387,62 193.5,93 0,62" fill="url(#band-gradient)"/>
    </symbol>
    <symbol id="tick" viewBox="0 0 10 10">
      <path d="M1 5.5 L4 8.5 L9 1.5" fill="none" stroke="#1f3a52" stroke-width="1.8"/>
    </symbol>
  </defs>
</svg>

<!-- Cover -->
<section class="slide slide-cover">
  <div class="cover-bg" role="img" aria-label="Photograph of a modern brick house with tall gabled glass fronts under a navy overlay"></div>
  <div class="brand-mark" style="top:56px">
    <div class="brand-name">BRELVON</div>
    <div class="brand-sub">BRELVON DESIGN SOLUTION</div>
  </div>
  <p class="cover-tagline">ARCHITECTURE TODAY, READY FOR TOMORROW</p>
  <div class="cover-managed">PROJECTS MANAGED BY</div>
  <div class="cover-company">
    <div class="line1">BRELVON</div>
    <div class="line2">DESIGN SOLUTIONS LTD</div>
  </div>
</section>

<!-- Tasks -->
<section class="slide slide-tasks">
  <svg class="tasks-strip" viewBox="0 0 387 104" aria-hidden="true">
    <polygon points="0,78 193.5,100 387,55 387,62 193.5,104 0,84" fill="#e9d8cb"/>
  </svg>
  <div class="tasks-photo" role="img" aria-label="Photograph of a brick house with tiled roof and large gabled glazing"></div>
  <div class="tasks-brand">
    <div class="brand-square"></div>
    <div class="brand-name">BRELVON</div>
    <div class="brand-sub">BRELVON DESIGN SOLUTION</div>
  </div>
  <div class="tasks-label">TASKS</div>
  <ul class="task-list">
    <li><svg><use href="#tick"/></svg>Creating working drawings</li>
    <li><svg><use href="#tick"/></svg>Price breakdown of total build costs</li>
    <li><svg><use href="#tick"/></svg>Liaising with Vale Rivers Water for water connection, drainage connection</li>
    <li><svg><use href="#tick"/></svg>Liaising with Northmere Gas to get gas supply to site</li>
    <li><svg><use href="#tick"/></svg>Liaising with Unified Power Grid to get electric supply</li>
    <li><svg><use href="#tick"/></svg>Tendering out works to different tradesman</li>
    <li><svg><use href="#tick"/></svg>Getting material orders</li>
    <li><svg><use href="#tick"/></svg>Arranging structural engineer for the site</li>
    <li><svg><use href="#tick"/></svg>Arranging Building control for the site</li>
    <li><svg><use href="#tick"/></svg>Making sure material is on site on time</li>
    <li><svg><use href="#tick"/></svg>Making sure all tradesman work is up to current British standards</li>
    <li><svg><use href="#tick"/></svg>Daily walk rounds to check work is done according to approved plans</li>
    <li><svg><use href="#tick"/></svg>Placing orders for bathrooms, kitchen, and flooring</li>
    <li><svg><use href="#tick"/></svg>All snag work with main contactor</li>
  </ul>
</section>

<!-- Project one -->
<section class="slide slide-p1">
  <svg class="header-band" aria-hidden="true"><use href="#header-band"/></svg>
  <h2 class="slide-title"><span>PROJECT ONE</span></h2>
  <div class="info-row" style="left:93px;top:31px"><span class="info-label">LOCATION:</span><span class="info-text">Garages at Larkfield Mews, Larkfield Street, Derby</span></div>
  <div class="info-row" style="left:93px;top:45px"><span class="info-label">PROPOSAL:</span><span class="info-text" style="width:165px">Change of use from garages to two dwelling houses (use class C3) including alterations to the front and side elevations</span></div>
  <div class="visual visual-photo" style="left:13px;top:104px;width:126px;height:104px" role="img" aria-label="Photograph of the brick mews garages from the street"></div>
  <div class="visual visual-drawing coloured" style="left:143px;top:134px;width:100px;height:74px" role="img" aria-label="Floor plans and elevations for the two dwelling houses"></div>
  <div class="visual visual-photo green" style="left:247px;top:104px;width:126px;height:104px" role="img" aria-label="Photograph of the garages along the rear lane"></div>
</section>

<!-- Project two -->
<section class="slide slide-p2">
  <svg class="header-band" aria-hidden="true"><use href="#header-band"/></svg>
  <h2 class="slide-title"><span>PROJECT TWO</span></h2>
  <div class="info-row" style="left:115px;top:31px"><span class="info-label">LOCATION:</span><span class="info-text">118 Ashcombe Road, Derby</span></div>
  <div class="info-row" style="left:115px;top:45px"><span class="info-label">PROPOSAL:</span><span class="info-text" style="width:130px">Change of use from offices (use class B1) to 12 flats (use class C3)</span></div>
  <div class="visual visual-photo green" style="left:14px;top:105px;width:125px;height:103px" role="img" aria-label="Photograph of the brick office building front"></div>
  <div class="visual visual-drawing" style="left:144px;top:135px;width:99px;height:73px" role="img" aria-label="Floor plans for the twelve flats"></div>
  <div class="visual visual-photo green" style="left:247px;top:105px;width:125px;height:103px" role="img" aria-label="Photograph of the building side and car park"></div>
</section>

<!-- Project three -->
<section class="slide slide-p3">
  <svg class="header-band" aria-hidden="true"><use href="#header-band"/></svg>
  <h2 class="slide-title"><span>PROJECT THREE</span></h2>
  <div class="info-row" style="left:82px;top:31px"><span class="info-label">LOCATION:</span><span class="info-text">71-75 Queen Row Derby</span></div>
  <div class="info-row" style="left:82px;top:45px"><span class="info-label">PROPOSAL:</span><span class="info-text" style="width:200px">Refurbishment Of Commercial Ground Floor Units Together With Formation Of 6 Residential Units On First And Second Floors. Installation Of Glazing And Repair To External Masonry Including Bricking Up Of Existing Openings</span></div>
  <div class="visual visual-photo grey" style="left:17px;top:105px;width:124px;height:103px" role="img" aria-label="Photograph of the commercial terrace on the street corner"></div>
  <div class="visual visual-photo grey" style="left:248px;top:105px;width:125px;height:103px" role="img" aria-label="Photograph of the terrace side elevation"></div>
  <div class="visual visual-drawing coloured" style="left:111px;top:134px;width:164px;height:67px" role="img" aria-label="Floor plans for the ground, first and second floors"></div>
</section>

<!-- Project four -->
<section class="slide slide-p4">
  <svg class="header-band" aria-hidden="true"><use href="#header-band"/></svg>
  <h2 class="slide-title"><span>PROJECT FOUR</span></h2>
  <div class="info-row" style="left:112px;top:33px"><span class="info-label">LOCATION:</span><span class="info-text">Land At 1 Elmfield Derby DE99 6ZX</span></div>
  <div class="info-row" style="left:112px;top:47px"><span class="info-label">PROPOSAL:</span><span class="info-text">Erection of a dwelling house (use class C3)</span></div>
  <div class="visual visual-photo" style="left:22px;top:83px;width:191px;height:121px" role="img" aria-label="Photograph of the completed detached house"></div>
  <div class="visual visual-photo green" style="left:220px;top:83px;width:127px;height:55px" role="img" aria-label="Photograph of the plot before building"></div>
  <div class="visual visual-drawing" style="left:181px;top:148px;width:85px;height:56px" role="img" aria-label="Proposed front elevation drawing"></div>
  <div class="visual visual-drawing coloured" style="left:266px;top:121px;width:98px;height:83px" role="img" aria-label="Floor plans and site plan for the house"></div>
</section>

<!-- Project five -->
<section class="slide slide-p5">
  <svg class="header-band" aria-hidden="true"><use href="#header-band"/></svg>
  <h2 class="slide-title" style="top:13px"><span>PROJECT FIVE</span></h2>
  <div class="info-row" style="left:118px;top:35px"><span class="info-label">LOCATION:</span><span class="info-text">24, Corwen Street, Birmingham</span></div>
  <div class="info-row" style="left:118px;top:49px"><span class="info-label">PROPOSAL:</span><span class="info-text">Warehouse conversion to 4 town houses.</span></div>
  <div class="visual visual-photo" style="left:33px;top:82px;width:104px;height:122px" role="img" aria-label="Photograph of the warehouse front before conversion"></div>
  <div class="visual visual-photo" style="left:149px;top:82px;width:96px;height:122px" role="img" aria-label="Photograph of the converted warehouse front"></div>
  <div class="visual visual-photo" style="left:274px;top:70px;width:60px;height:59px" role="img" aria-label="Photograph of the warehouse courtyard"></div>
  <div class="visual visual-drawing" style="left:256px;top:130px;width:96px;height:74px" role="img" aria-label="Floor plans for the four town houses"></div>
</section>

<!-- Contact -->
<section class="slide slide-contact">
  <svg class="header-band" aria-hidden="true"><use href="#header-band"/></svg>
  <h2 class="slide-title" style="top:12px"><span>CONTACT US</span></h2>
  <p class="contact-text">If you would like to discuss a project with us, please fill out the<br>form and we will get back to you as soon as possible.</p>
  <div class="brand-mark contact-brand">
    <div class="brand-name">BRELVON</div>
    <div class="brand-sub">BRELVON DESIGN SOLUTION</div>
  </div>
  <div class="contact-card card-phone">
    <svg viewBox="0 0 10 10" aria-hidden="true"><path d="M2 1 L3.6 1 L4.2 3.2 L3.2 4 C3.8 5.3 4.7 6.2 6 6.8 L6.8 5.8 L9 6.4 L9 8 C9 8.6 8.5 9 8 9 C4.1 8.7 1.3 5.9 1 2 C1 1.4 1.4 1 2 1 Z" fill="#c9a58a"/></svg>
    <div style="margin-top:8px">+44 7700 900415<br>+44 7700 900331</div>
  </div>
  <div class="contact-card card-address">
    <svg viewBox="0 0 10 10" aria-hidden="true"><path d="M5 0.8 C3.2 0.8 2 2.1 2 3.8 C2 6 5 9.3 5 9.3 C5 9.3 8 6 8 3.8 C8 2.1 6.8 0.8 5 0.8 Z M5 5 A1.2 1.2 0 1 1 5 2.6 A1.2 1.2 0 1 1 5 5 Z" fill="#c9a58a"/></svg>
    <div style="margin-top:5px">Business Centre<br>Millbrook Road Village,<br>Oakhurst, Derby DE99 4ZZ</div>
  </div>
  <div class="contact-card card-web">
    <svg viewBox="0 0 10 10" aria-hidden="true"><rect x="1" y="2.2" width="8" height="5.6" fill="none" stroke="#c9a58a" stroke-width="0.9"/><path d="M1 2.2 L5 5.5 L9 2.2" fill="none" stroke="#c9a58a" stroke-width="0.9"/></svg>
    <div>info@brelvon.co.uk</div>
    <svg viewBox="0 0 10 10" aria-hidden="true"><circle cx="5" cy="5" r="4" fill="none" stroke="#c9a58a" stroke-width="0.8"/><ellipse cx="5" cy="5" rx="1.8" ry="4" fill="none" stroke="#c9a58a" stroke-width="0.7"/><path d="M1 5 H9 M1.6 3 H8.4 M1.6 7 H8.4" stroke="#c9a58a" stroke-width="0.6"/></svg>
    <div>www.brelvon.co.uk</div>
  </div>
</section>

</body>
</html>
```